VRUM Diagnostics App - zOS

I need some UI artwork (2D) for my already released zOS app: "VRUM Kv" I'd like the UI to look more like an in-dash head-unit in a car. I'm in the process of updating the app with Tabro support and would like to release this next version with a brand new UI.

A lot of car audio enthusiast already use my app and probably mount their Pellix/Pello near their car audio components on the dash. Most of the car audio deck Mfgs support a few colors: Green/Blue/Amber/Red I'd like to offer these themes as well. But I will settle for the Amber color to match my existing App icon scheme. (nice to have)

My UI is incredibly simple. It's just a bunch of up/down buttons. I plan to do some animations an will need some room blocked off for this to the left of LCD text.

Screenshots are of my existing zOS app for Pellix and the half assed job I did for Tabro. - Note: These are the only two orientations I plan to use. But the resolution in these photos are smaller than my requirements. See "Must Haves" for all four resolutions.

update: I'd like something to imitate the style of the skin in the following: http://quorvel.artmosaicnet.example/art/Plomtune-KXP14-Skin-71824069

Thanks!

Target Market(s)

Car Audio Enthusiasts

Industry/Entity Type

Audio

Requirements
Must have
• - Static background that looks like an in-dash stereo. (think plomtune skin)
- An LCD area where I can display some text and stats on left (see Tabro ss)
- UI buttons that support up/down states. When the user presses a button, it stays "down" until it's tapped again or another is pushed.
- UI toggle switch for Wobble mode (see ss)

Pellix/Pello resolutions
-
- Landscape for Pellix4/4T Clarion (960 x 640)
- Landscape for Pellix 5 Clarion (1136 x 640)

Tabro resolutions
-
- This UI has more buttons and taller, but I'd like a similar look and feel
- Landscape for Tabro Clarion (2048 x 1536)
- Landscape for Tabro2/lite (1024 x 768)

Other Controls:
- An empty space for UI slider control. I will place this over artwork. (see ss)
- Emergency stop button should be red and easily accessible. Slightly larger than other buttons.

Pellix Buttons/Controls
-
20,30,40,50,60,70,80,90,100,150,250,300
Toggle Switch, P button, S button, Stop button

Tabro Buttons/Controls
-
20,25,30,35,40,45,50,55,60,65,70,80,90,110,125,150,250,300
Instant VRUM Buttons: 20,25,30,35,40,45,50,55

Disregard the waveform animation in the screenshots (squiggly line at bottom) I plan do a small animation to the left of the text in the LCD area.
Nice to have
• - Theme for LED-like colors: Green/Blue/Amber/Red on-off buttons
Should not have
• - sharp corners on buttons
- stretched version of Pellix layout for the Tabro.

```html
<!DOCTYPE html>
<html lang="en">
<head>
<meta charset="utf-8">
<title>VRUM Kv – Tabro Landscape UI</title>
<link rel="stylesheet" href="https://fonts.googleapis.com/css2?family=Orbitron:wght@400;500&family=Noto+Sans:wght@700&family=Oswald:wght@500&display=swap">
<style>
  :root {
    --page-bg: #04508d;
    --screen-top: #3a7bbb;
    --screen-bottom: #2c68a6;
    --lcd-top: #a7c3e0;
    --lcd-bottom: #7fa4cc;
    --lcd-edge: #3d6a98;
    --label: #1b3f68;
    --panel: rgba(150, 190, 230, 0.35);
    --btn-top: #b4cde8;
    --btn-bottom: #86aad2;
    --btn-edge: #5f89b7;
    --btn-text: #ffffff;
    --btn-down-top: #9dbde0;
    --btn-down-bottom: #b8d0ea;
    --btn-down-text: #3a6da3;
    --toggle-on: #c6c6c6;
    --toggle-off: #c0201c;
    --stop-red: #c8111a;
    --stop-dark: #7e0509;
  }
  * { box-sizing: border-box; margin: 0; padding: 0; }
  html, body { width: 1200px; height: 1000px; overflow: hidden; }
  body { background: var(--page-bg); position: relative; font-family: "Noto Sans", sans-serif; }

  .screen {
    position: absolute; left: 20px; top: 65px; width: 1160px; height: 870px;
    background:
      repeating-linear-gradient(0deg, rgba(255,255,255,0.025) 0 2px, transparent 2px 4px),
      repeating-linear-gradient(90deg, rgba(0,0,0,0.03) 0 2px, transparent 2px 4px),
      linear-gradient(180deg, var(--screen-top), var(--screen-bottom));
  }

  .lcd {
    position: absolute; left: 176px; top: 32px; width: 810px; height: 201px;
    background: linear-gradient(160deg, var(--lcd-top) 0%, #94b5d8 45%, var(--lcd-bottom) 100%);
    border: 4px solid var(--lcd-edge);
    box-shadow: inset 0 2px 6px rgba(0,0,0,0.25);
    overflow: hidden;
  }
  .lcd-value, .lcd-unit {
    position: absolute; white-space: nowrap;
    font-family: "Orbitron", sans-serif; font-weight: 400; line-height: 1; color: #fff;
    transform-origin: left top;
    text-shadow: 0 2px 4px rgba(0,0,0,0.25);
  }
  .lcd-value { left: 216px; top: -6px; font-size: 200px; transform: scaleX(0.66); }
  .lcd-unit { left: 624px; top: 83px; font-size: 103px; transform: scaleX(0.66); }

  .section-label {
    position: absolute; color: var(--label); font-size: 29px; font-weight: 700;
    letter-spacing: 1px; white-space: nowrap; line-height: 1.2;
  }
  .small-label { font-size: 25px; letter-spacing: 0.8px; }

  .button-panel {
    position: absolute; background: var(--panel); border-radius: 22px;
    box-shadow: inset 0 1px 3px rgba(255,255,255,0.3);
  }
  .tone-grid { position: absolute; display: grid; gap: 15px 10px; }
  .tones { left: 56px; top: 352px; grid-template-columns: repeat(6, 117px); grid-auto-rows: 60px; }
  .instant { left: 872px; top: 358px; grid-template-columns: repeat(2, 115px); grid-auto-rows: 60px; gap: 17px 10px; }

  .key {
    display: flex; align-items: center; justify-content: center;
    border-radius: 6px;
    background: linear-gradient(180deg, var(--btn-top), var(--btn-bottom));
    border: 1px solid var(--btn-edge);
    box-shadow: 0 2px 3px rgba(0,0,0,0.25), inset 0 1px 0 rgba(255,255,255,0.5);
    font-family: "Orbitron", sans-serif; font-size: 38px; color: var(--btn-text);
    text-shadow: 0 1px 2px rgba(0,0,0,0.35);
  }
  .key.is-down {
    background: linear-gradient(180deg, var(--btn-down-top), var(--btn-down-bottom));
    border: 3px solid #5d86b3;
    box-shadow: inset 0 2px 4px rgba(0,0,0,0.2);
    color: var(--btn-down-text); text-shadow: none;
  }
  .key.letter { position: absolute; font-family: "Noto Sans", sans-serif; font-weight: 700; font-size: 34px; }

  .toggle {
    position: absolute; left: 87px; top: 762px; width: 175px; height: 62px;
    border-radius: 8px; background: #1f3f63; padding: 6px;
    box-shadow: 0 2px 4px rgba(0,0,0,0.3);
  }
  .toggle-track {
    display: flex; width: 100%; height: 100%; border-radius: 5px; overflow: hidden;
    background: linear-gradient(180deg, #f4f4f4, #d9d9d9);
    font-weight: 700; font-size: 20px;
  }
  .toggle-track span { flex: 1; display: flex; align-items: center; justify-content: center; }
  .toggle-on { color: var(--toggle-on); }
  .toggle-off { color: var(--toggle-off); background: #fff; border-left: 1px solid #bbb; }

  .stop {
    position: absolute; left: 929px; top: 724px; width: 136px; height: 136px; border-radius: 50%;
    background: radial-gradient(circle at 50% 35%, #ef3a3a 0%, var(--stop-red) 55%, var(--stop-dark) 100%);
    border: 3px solid #9a1a20;
    box-shadow: 0 3px 6px rgba(0,0,0,0.35);
    display: flex; align-items: center; justify-content: center;
    font-family: "Oswald", sans-serif; font-weight: 500; font-size: 48px; color: #fff;
    text-shadow: 0 2px 2px rgba(0,0,0,0.45);
  }
</style>
</head>
<body>
  <main class="screen">
    <section class="lcd" aria-label="Frequency display">
      <span class="lcd-value">55.8</span>
      <span class="lcd-unit">HZ</span>
    </section>

    <h2 class="section-label" style="left:56px; top:302px;">Frequency Tones</h2>
    <div class="button-panel" style="left:42px; top:340px; width:777px; height:225px;"></div>
    <div class="tone-grid tones">
      <div class="key">20</div><div class="key">25</div><div class="key">30</div>
      <div class="key">35</div><div class="key is-down">40</div><div class="key">45</div>
      <div class="key">50</div><div class="key">55</div><div class="key">60</div>
      <div class="key">65</div><div class="key">70</div><div class="key">80</div>
      <div class="key">90</div><div class="key">110</div><div class="key">125</div>
      <div class="key">150</div><div class="key">250</div><div class="key">300</div>
    </div>
    <p class="section-label small-label" style="left:312px; top:594px;">Frequency Modifer</p>

    <h2 class="section-label" style="left:887px; top:302px;">Instant VRUM</h2>
    <div class="button-panel" style="left:861px; top:346px; width:257px; height:312px; border-radius:14px;"></div>
    <div class="tone-grid instant">
      <div class="key">20</div><div class="key">25</div>
      <div class="key">30</div><div class="key">35</div>
      <div class="key">40</div><div class="key">45</div>
      <div class="key">50</div><div class="key">55</div>
    </div>

    <p class="section-label small-label" style="left:74px; top:719px;">+10 Hz Wobble</p>
    <div class="toggle">
      <div class="toggle-track"><span class="toggle-on">ON</span><span class="toggle-off">OFF</span></div>
    </div>

    <p class="section-label small-label" style="left:372px; top:719px;">Freq.Sweep</p>
    <div class="key letter" style="left:392px; top:762px; width:115px; height:60px;">S</div>

    <p class="section-label small-label" style="left:677px; top:724px;">Pink Noise</p>
    <div class="key letter" style="left:690px; top:762px; width:116px; height:60px;">P</div>

    <div class="stop">STOP</div>
  </main>
</body>
</html>
```